Need Stunning, Visual Tree Identification Booklet

We are looking for a magazine/booklet style design for tree and plant identification. They need to be organized according to tree/plant type and contain a picture and tree/plant information. I would like to see 4 trees/plants per page. I will be including links for all the information needed but you will be responsible for gathering pictures as we have none to provide. This is not a booklet that will be sold or given out, it is solely to be used by our company internally for training and for presenting during sales meetings.

Target Market(s)

To be used by our sales staff when meeting with customers and selling trees and plants.

Industry/Entity Type

Landscape Gardening

Font styles to use
Serif

Requirements
Must have
• Attractive design that makes it easy to read and visual the trees and plants shown in the booklet. Design must be done in Adobe Illustrator or Adobe InDesign. Every tree/plant must have a picture, description, common name, Botanical name, Height, Width, Growth Rate, Function, Hardiness and Water Use. Would like to fit 4 trees/plants per page. Attached is a category outline.
Nice to have
• Clean, professional look. Using greens, whites and blacks

```html
<!DOCTYPE html>
<html lang="en">
<head>
<meta charset="utf-8">
<title>Citrus &amp; Fruit – Tree Identification Booklet</title>
<link href="https://fonts.googleapis.com/css2?family=Merriweather:wght@300;400;700&display=swap" rel="stylesheet">
<style>
  :root {
    --green: #2aa54a;
    --black: #000;
    --white: #fff;
    --ink: #555;
    --title: #444;
    --mint: #d8ecd5;
    --backdrop: #d9d9d9;
  }
  * { box-sizing: border-box; margin: 0; padding: 0; }
  html, body { width: 1200px; height: 1200px; overflow: hidden; background: var(--backdrop); }
  body { font-family: "Merriweather", Georgia, serif; color: var(--ink); }

  .page {
    position: absolute; left: 152px; top: 21px;
    width: 895px; height: 1157px; background: var(--white);
  }
  .rule { position: absolute; }
  .rule--green-top { top: 51px; height: 7px; background: var(--green); }
  .rule--black-top { top: 62px; height: 12px; background: var(--black); }
  .rule--left { left: 0; width: 48px; }
  .rule--right { left: 202px; right: 0; }

  .brand {
    position: absolute; left: 52px; top: 52px; width: 146px; height: 150px;
    display: flex; flex-direction: column; align-items: center; justify-content: center; gap: 10px;
  }
  .brand__dot { width: 84px; height: 84px; border-radius: 50%; background: var(--green); }
  .brand__name { font-size: 17px; font-weight: 700; color: var(--black); letter-spacing: 1px; white-space: nowrap; }

  .page-title {
    position: absolute; right: 53px; top: 102px;
    font-size: 44px; font-weight: 300; color: var(--title);
  }

  .section-band {
    position: absolute; left: 53px; top: 224px; width: 789px; height: 35px;
    background: var(--black); color: var(--white);
    font-size: 17px; font-weight: 300; padding: 6px 15px;
  }

  .entries { position: absolute; left: 53px; top: 270px; width: 789px; }
  .entry { display: flex; gap: 23px; height: 200px; }
  .entry__photo { width: 242px; height: 183px; flex: none; }
  .photo--orange-pair { background: radial-gradient(circle at 55% 45%, #f7961c 0 28%, #e9791a 40%, #4f6b37 62%, #2e4424 100%); }
  .photo--navel { background: radial-gradient(circle at 68% 62%, #f4b21b 0 16%, #7a9a55 30%, #3f6a2e 60%, #dfe9ee 100%); }
  .photo--valencia { background: radial-gradient(circle at 50% 50%, #f07a22 0 30%, #c8611e 42%, #3a5a28 70%, #23391b 100%); }

  .entry__body { flex: 1; }
  .entry__name { font-size: 17.5px; font-weight: 700; color: var(--green); margin: 0 0 4px; }
  .entry__text { font-size: 11.6px; font-weight: 300; line-height: 17.5px; margin-bottom: 6px; }

  .specs { width: 100%; border-collapse: separate; border-spacing: 2px 0; margin-left: -2px; width: calc(100% + 4px); table-layout: fixed; }
  .specs th {
    background: var(--black); color: #bbb; font-weight: 300; font-size: 11px;
    line-height: 14px; height: 35px; text-align: left; padding: 2px 5px; vertical-align: top;
  }
  .specs td {
    background: var(--mint); font-size: 11px; font-weight: 300; height: 19px; padding: 3px 5px 0;
  }

  .page-number {
    position: absolute; left: 73px; top: 1062px; width: 62px; height: 62px;
    background: var(--green); border: 3px solid var(--white); color: var(--white);
    font-size: 19px; font-weight: 300; display: flex; align-items: center; justify-content: center;
    z-index: 2;
  }
  .rule--green-bottom { left: 0; right: 0; top: 1097px; height: 5px; background: var(--green); }
  .rule--black-bottom { left: 0; right: 0; top: 1113px; height: 44px; background: var(--black); }
</style>
</head>
<body>
<main class="page">
  <div class="rule rule--green-top rule--left"></div>
  <div class="rule rule--green-top rule--right"></div>
  <div class="rule rule--black-top rule--left"></div>
  <div class="rule rule--black-top rule--right"></div>

  <div class="brand">
    <span class="brand__dot"></span>
    <span class="brand__name">CANOPY CREW</span>
  </div>

  <h1 class="page-title">Citrus &amp; Fruit</h1>

  <div class="section-band">Orange</div>

  <section class="entries">
    <article class="entry">
      <div class="entry__photo photo--orange-pair" role="img" aria-label="Two ripe Arizona sweet oranges among dark green leaves"></div>
      <div class="entry__body">
        <h2 class="entry__name">Citrus Trees - Arizona Sweet Orange</h2>
        <p class="entry__text">The Arizona Sweet Orange produces medium sized oranges with bright orange flesh. They are slightly harder to peel than a Navel Orange and that is what causes this orange to be considered more of a juice orange.</p>
        <p class="entry__text">Arizona Sweet Oranges are very juicy, have a nice sweet flavor, and have few if any seeds. It is a medium sized tree that does well in our climate.</p>
        <table class="specs">
          <tr><th>common name</th><th>Botanical name</th><th>Height</th><th>Width</th><th>Growth Rate</th><th>Function</th><th>Hardiness</th><th>Water Use</th></tr>
          <tr><td>Arizona</td><td>Arizona</td><td>10.55</td><td>6.5</td><td>.5</td><td>text</td><td>text</td><td>text goes</td></tr>
        </table>
      </div>
    </article>

    <article class="entry">
      <div class="entry__photo photo--navel" role="img" aria-label="Washington navel orange hanging on a leafy branch"></div>
      <div class="entry__body">
        <h2 class="entry__name">Washington Navel Orange</h2>
        <p class="entry__text">Washington Navel Orange-- Tree medium, drooping, round. Fruit medium to large, thick-skinned, juicy. Considered the world's finest orange for eating, navels are seedless, and they peel and segment easily. Harvest December to March.</p>
        <table class="specs">
          <tr><th>common name</th><th>Botanical name</th><th>Height</th><th>Width</th><th>Growth Rate</th><th>Function</th><th>Hardiness</th><th>Water Use</th></tr>
          <tr><td>Arizona</td><td>Arizona</td><td>10.55</td><td>6.5</td><td>.5</td><td>text</td><td>text</td><td>text goes</td></tr>
        </table>
      </div>
    </article>

    <article class="entry">
      <div class="entry__photo photo--valencia" role="img" aria-label="Cluster of Valencia oranges on the tree"></div>
      <div class="entry__body">
        <h2 class="entry__name">Valencia Orange</h2>
        <p class="entry__text">Tree medium, round. Fruit small to medium-sized, thin-skinned, full of excellent tasting juice. Best juice orange, difficult to peel. Fruit stores well on tree. Harvest February to June.</p>
        <table class="specs">
          <tr><th>common name</th><th>Botanical name</th><th>Height</th><th>Width</th><th>Growth Rate</th><th>Function</th><th>Hardiness</th><th>Water Use</th></tr>
          <tr><td>Arizona</td><td>Arizona</td><td>10.55</td><td>6.5</td><td>.5</td><td>text</td><td>text</td><td>text goes</td></tr>
        </table>
      </div>
    </article>

    <article class="entry">
      <div class="entry__photo photo--valencia" role="img" aria-label="Cluster of Valencia oranges on the tree"></div>
      <div class="entry__body">
        <h2 class="entry__name">Valencia Orange</h2>
        <p class="entry__text">Tree medium, round. Fruit small to medium-sized, thin-skinned, full of excellent tasting juice. Best juice orange, difficult to peel. Fruit stores well on tree. Harvest February to June.</p>
        <table class="specs">
          <tr><th>common name</th><th>Botanical name</th><th>Height</th><th>Width</th><th>Growth Rate</th><th>Function</th><th>Hardiness</th><th>Water Use</th></tr>
          <tr><td>Arizona</td><td>Arizona</td><td>10.55</td><td>6.5</td><td>.5</td><td>text</td><td>text</td><td>text goes</td></tr>
        </table>
      </div>
    </article>
  </section>

  <div class="rule rule--green-bottom"></div>
  <div class="rule rule--black-bottom"></div>
  <div class="page-number">01</div>
</main>
</body>
</html>
```